IT Consultancy Web Site

We need a twitter bootstrap, hero based designed for our IT Consultancy firm based in Adelaide, Australia called "Brenwick IT Consulting". We provide custom software development. We have some core areas of the site we wish to develop further at a later point. A blog, an ecommerce shop, and products / services listings - All three of these should have clearly visible navigation below the hero.

The final design should be clean and minimalist. It should communicate professionalism and elegance.

Industry/Entity Type

Shop

Requirements
Nice to have
• We currently do not have a logo, so inclusion of something simple in the design would be a bonus

```html
<!DOCTYPE html>
<html lang="en">
<head>
<meta charset="utf-8">
<title>Brenwick IT Consulting</title>
<link rel="stylesheet" href="https://fonts.googleapis.com/css2?family=Oswald:wght@600;700&family=Arvo:wght@400;700&family=Arimo:wght@400;700&family=Questrial&family=Tinos:wght@400;700&family=Gelasio:ital@1&family=Roboto+Condensed:wght@400&display=swap">
<style>
:root{
  --dark:#2b2b2b;
  --orange:#f15a13;
  --navy:#1d2c5a;
  --green:#72b51a;
  --green-deep:#5f9a12;
  --green-text:#84c225;
  --text:#555555;
  --rule:#dddddd;
}
*{margin:0;padding:0;box-sizing:border-box}
html,body{width:1200px;height:2365px;overflow:hidden;background:#fff}
body{position:relative;font-family:"Arimo",Arial,sans-serif;color:var(--text)}
.abs{position:absolute}

/* header */
.site-header{position:absolute;left:0;top:0;width:1200px;height:93px;background:linear-gradient(#333,#262626)}
.brand{left:142px;top:20px;font-weight:700;font-size:21px;line-height:26px;color:var(--green-text)}
.brand small{display:block;font-size:17px;font-weight:700}
.main-nav{left:479px;top:29px;display:flex;font-family:"Tinos",serif;font-size:16px;color:#e6e6e6}
.main-nav a{color:inherit;text-decoration:none;padding:0 16px;line-height:28px;height:28px}
.main-nav a.active{background:var(--orange);color:#fff;border-radius:14px;padding:0 18px;font-weight:700;margin-right:8px}
.social-top{left:955px;top:29px;display:flex;gap:10px}
.social-top span{width:28px;height:28px;border-radius:50%;background:#8a8a8a;display:block}

/* hero */
.hero{left:0;top:93px;width:1200px;height:508px}
.hero-photo{position:absolute;inset:0;background:linear-gradient(90deg,#dfe2e4 0%,#f4f5f6 40%,#e9ebec 60%,#c9cdd0 100%)}
.hero-person{position:absolute;left:400px;top:10px;width:620px;height:498px;background:radial-gradient(ellipse at 60% 45%,#3a3a45 0%,#5a5a66 30%,rgba(230,232,234,0) 70%)}
.hero-title{left:140px;top:98px;font-family:"Oswald",sans-serif;font-weight:700;font-size:82px;line-height:82px;color:var(--orange);letter-spacing:1px}
.hero-sub{left:142px;top:176px;font-family:"Oswald",sans-serif;font-weight:600;font-size:29px;line-height:34px;color:var(--navy);letter-spacing:1px}
.hero-text{left:142px;top:214px;width:475px;font-family:"Roboto Condensed",sans-serif;font-size:17px;line-height:24px;color:#2f2f2f}
.hero-arrows{left:140px;top:400px;display:flex;gap:2px}
.hero-arrows span{width:45px;height:46px;background:rgba(80,80,80,.75);display:flex;align-items:center;justify-content:center}

/* welcome */
.welcome{left:0;top:601px;width:1200px;height:203px;background:var(--green);color:#fff;text-align:center}
.welcome h1{position:absolute;left:0;right:0;top:28px;font-family:"Questrial",sans-serif;font-weight:400;font-size:26px;line-height:34px}
.welcome p{position:absolute;left:160px;right:160px;top:76px;font-family:"Questrial",sans-serif;font-size:15px;line-height:26px}
.section-links{position:absolute;left:0;right:0;top:166px;display:flex;justify-content:center;gap:12px}
.section-links a{display:block;height:26px;line-height:26px;padding:0 18px;border-radius:13px;background:var(--green-deep);color:#fff;font-family:"Arimo",sans-serif;font-size:13px;font-weight:700;text-decoration:none;letter-spacing:.5px}

/* section rule titles */
.rule-title{left:0;width:1200px;text-align:center;font-family:"Arvo",serif;font-size:29px;color:#222;font-weight:400}
.rule{position:absolute;height:1px;background:var(--rule)}

/* why */
.why-title{left:142px;top:842px;font-family:"Arvo",serif;font-weight:400;font-size:32px;line-height:38px;color:var(--orange)}
.why-text{left:142px;top:950px;width:460px;font-size:18.5px;line-height:31px;color:#7a7a7a}
.monitor{left:680px;top:851px;width:378px;height:321px;border-radius:8px;background:linear-gradient(#1a1a1a 0%,#1a1a1a 78%,#d9d9d9 78%,#bdbdbd 100%)}

/* services */
.service{width:300px}
.service h3{font-weight:400;font-size:18.5px;color:#333;display:flex;align-items:center;gap:12px;height:36px}
.service p{margin-top:12px;font-size:13.5px;line-height:23px;color:#666}
.service a{color:var(--orange);text-decoration:none}

/* product */
.product{left:0;top:1444px;width:1200px;height:433px;background:linear-gradient(90deg,#5a5a5a 0%,#2e2e2e 45%,#262626 100%)}
.product-photo{position:absolute;left:190px;top:20px;width:380px;height:413px;background:radial-gradient(ellipse at 50% 50%,#c08a8f 0%,#7a6a6c 35%,rgba(50,50,50,0) 70%)}
.product h2{position:absolute;left:567px;top:38px;font-family:"Arvo",serif;font-weight:400;font-size:30.5px;color:#fff}
.product .rule{left:567px;top:86px;width:490px;background:#555}
.ticks{position:absolute;left:573px;top:100px;list-style:none;font-size:15.5px;line-height:31px;color:#e4e4e4}
.ticks li{display:flex;gap:12px;align-items:flex-start}
.ticks li svg{margin-top:10px;flex:none}
.btn{position:absolute;left:569px;top:340px;width:99px;height:28px;border-radius:14px;background:var(--orange);color:#fff;font-size:14px;line-height:28px;text-align:center}

/* testimonials */
.quote{left:142px;top:1980px;width:916px;font-family:"Gelasio",serif;font-style:italic;font-size:16px;line-height:27px;color:#666;text-indent:34px}
.quote-mark{left:138px;top:1966px;font-family:"Gelasio",serif;font-size:56px;color:#ccc;line-height:56px}

/* footer */
.site-footer{left:0;top:2092px;width:1200px;height:273px;background:var(--dark);color:#d5d5d5}
.site-footer h4{position:absolute;font-weight:400;font-size:16px;color:var(--green-text)}
.foot-list{position:absolute;list-style:none;font-size:13px;line-height:22px;color:#e0e0e0}
.vline{position:absolute;top:0;width:1px;height:198px;background:#444}
.email{position:absolute;left:590px;top:69px;width:200px;height:27px;background:#fff;border-radius:14px;font-family:"Tinos",serif;font-size:12px;color:#555;line-height:27px;padding-left:10px}
.email-btn{position:absolute;left:782px;top:67px;width:31px;height:31px;border-radius:50%;background:var(--orange);border:3px solid #333}
.share{position:absolute;left:593px;top:116px;font-size:13px}
.social-foot{position:absolute;left:595px;top:140px;display:flex;gap:6px}
.social-foot span{width:31px;height:31px;border-radius:50%;display:block}
.copyright{position:absolute;left:0;right:0;top:238px;text-align:center;font-size:13px;color:#cfcfcf}
</style>
</head>
<body>

<header class="site-header">
  <div class="brand abs">Brenwick IT<small>Consulting</small></div>
  <nav class="main-nav abs">
    <a class="active">Home</a><a>About Us</a><a>Services</a><a>Our Product</a><a>Contact Us</a>
  </nav>
  <div class="social-top abs"><span></span><span></span><span></span></div>
</header>

<section class="hero abs">
  <div class="hero-photo" role="img" aria-label="Bright office interior background"></div>
  <div class="hero-person" role="img" aria-label="Businessman in a suit working on a laptop at a desk with a lamp and coffee mug"></div>
  <div class="hero-title abs">CUNSULTING</div>
  <div class="hero-sub abs">SOFTWARE DEVELOPMENT WITH US</div>
  <p class="hero-text abs">We specialise in the implementation of Hosted Terminal Services Networks which provide significant advantages over traditional PC peer-to-peer networks.</p>
  <div class="hero-arrows abs">
    <span><svg width="12" height="18" viewBox="0 0 12 18"><path d="M9 2 3 9l6 7" fill="none" stroke="#ddd" stroke-width="1.5"/></svg></span>
    <span><svg width="12" height="18" viewBox="0 0 12 18"><path d="M3 2l6 7-6 7" fill="none" stroke="#ddd" stroke-width="1.5"/></svg></span>
  </div>
</section>

<section class="welcome abs">
  <svg class="abs" style="left:142px;top:40px" width="150" height="12" viewBox="0 0 150 12"><path d="M0 6h140M136 2l6 4-6 4" stroke="#a6d66a" fill="none" stroke-width="1.2"/></svg>
  <h1>WELCOME TO THE BRENWICK IT CONSULTING</h1>
  <svg class="abs" style="left:908px;top:40px" width="150" height="12" viewBox="0 0 150 12"><path d="M10 6h140M14 2 8 6l6 4" stroke="#a6d66a" fill="none" stroke-width="1.2"/></svg>
  <p>Lorem Ipsum is simply dummy text of the printing and typesetting industry. Lorem Ipsum has been the industry's standard dummy text ever since the 1500s, when an unknown printer took a galley of type and scramble to make a type specimen book. It has survived not only five centuries</p>
  <nav class="section-links"><a>Blog</a><a>Shop</a><a>Products &amp; Services</a></nav>
</section>

<h2 class="why-title abs">Why should you choose<br>The Servise</h2>
<div class="rule" style="left:142px;top:934px;width:473px"></div>
<p class="why-text abs">Lorem Ipsum is simply dummy text of the printing and typesetting industry. Lorem Ipsum has been the industry's standard dummy text ever since the 1500s, when an unknown printer took a galley of type and scrambled it to make a type specimen book.</p>
<div class="monitor abs" role="img" aria-label="Desktop monitor showing a colourful analytics dashboard"></div>

<div class="rule" style="left:142px;top:1219px;width:321px"></div>
<h2 class="rule-title abs" style="top:1199px">View Our Services</h2>
<div class="rule" style="left:739px;top:1219px;width:319px"></div>

<div class="service abs" style="left:142px;top:1276px">
  <h3><svg width="26" height="26" viewBox="0 0 26 26"><circle cx="13" cy="13" r="9" fill="none" stroke="#6aaa1e" stroke-width="4" stroke-dasharray="4 3"/><circle cx="13" cy="13" r="4" fill="#6aaa1e"/></svg>Make it your own</h3>
  <p>Lorem Ipsum is simply dummy text of printing and typesetting industry. Lorem Ipsum has been the industry. <a>Read more...</a></p>
</div>
<div class="service abs" style="left:459px;top:1276px">
  <h3><svg width="22" height="28" viewBox="0 0 22 28"><rect x="2" y="2" width="18" height="24" rx="3" fill="none" stroke="#6aaa1e" stroke-width="2.5"/><rect x="6" y="6" width="10" height="14" fill="#cfe8a8"/></svg>For every device.</h3>
  <p>Lorem Ipsum is simply dummy text of printing and typesetting industry. Lorem Ipsum has been the industry. <a>Read more...</a></p>
</div>
<div class="service abs" style="left:782px;top:1276px">
  <h3><svg width="28" height="22" viewBox="0 0 28 22"><path d="M2 20C6 10 12 7 18 7V2l8 8-8 8v-5c-6 0-11 2-16 7z" fill="#6aaa1e"/></svg>All services</h3>
  <p>Lorem Ipsum is simply dummy text of printing and typesetting industry. Lorem Ipsum has been the industry. <a>Read more...</a></p>
</div>

<section class="product abs">
  <div class="product-photo" role="img" aria-label="Woman in a pink sweater working on a laptop"></div>
  <h2>Click On Your Using Product</h2>
  <div class="rule"></div>
  <ul class="ticks">
    <li><svg width="14" height="12" viewBox="0 0 14 12"><path d="M1 6l4 4 8-9" fill="none" stroke="#8cc63f" stroke-width="2.5"/></svg><span>Lorem Ipsum is simply dummy text of the printing &amp; typesetting<br>industry, lorem ipsum.</span></li>
    <li><svg width="14" height="12" viewBox="0 0 14 12"><path d="M1 6l4 4 8-9" fill="none" stroke="#8cc63f" stroke-width="2.5"/></svg><span>Lorem ipsum dolor sit amet, consectetur adipiscing elit.</span></li>
    <li><svg width="14" height="12" viewBox="0 0 14 12"><path d="M1 6l4 4 8-9" fill="none" stroke="#8cc63f" stroke-width="2.5"/></svg><span>Mauris molestie lectus ut odio faucibus vulputate.</span></li>
    <li><svg width="14" height="12" viewBox="0 0 14 12"><path d="M1 6l4 4 8-9" fill="none" stroke="#8cc63f" stroke-width="2.5"/></svg><span>Curabitur hendrerit elit sit amet varius ultrices.</span></li>
    <li><svg width="14" height="12" viewBox="0 0 14 12"><path d="M1 6l4 4 8-9" fill="none" stroke="#8cc63f" stroke-width="2.5"/></svg><span>Donec eget nunc eget tellus facilisis rutrum eget sed sapien.</span></li>
    <li><svg width="14" height="12" viewBox="0 0 14 12"><path d="M1 6l4 4 8-9" fill="none" stroke="#8cc63f" stroke-width="2.5"/></svg><span>Sed et leo sed massa scelerisque luctus</span></li>
  </ul>
  <div class="btn">View All &#9656;</div>
</section>

<div class="rule" style="left:142px;top:1933px;width:321px"></div>
<h2 class="rule-title abs" style="top:1911px;font-size:31px">Testimonials</h2>
<div class="rule" style="left:739px;top:1933px;width:319px"></div>
<div class="quote-mark abs">&ldquo;</div>
<p class="quote abs">Lorem Ipsum is simply dummy text of the printing and typesetting industry. Lorem Ipsum has been the industry's standard dummy text ever asince the 1500s, when an unknown printer took a galley of type and scrambled it to make a type specimen book. It has survived not only five centuries, but also the leap into electronic typesetting.</p>

<footer class="site-footer abs">
  <h4 style="left:142px;top:38px">Services</h4>
  <ul class="foot-list" style="left:142px;top:65px">
    <li>Business Analysis</li><li>Systems Analysis</li><li>System Integration</li><li>Terminal Services Networks</li><li>Technical Support</li><li>Hardware &amp; Software Supply</li>
  </ul>
  <ul class="foot-list" style="left:341px;top:65px">
    <li>Installation &amp; Setup</li><li>System Maintenance</li><li>Application &amp; Hardware Support</li><li>Remote System &amp; User Support</li><li>No SLA Contracts</li>
  </ul>
  <div class="vline" style="left:561px"></div>
  <h4 style="left:593px;top:38px">Sign Up for updates</h4>
  <div class="email">Enter your email...</div>
  <div class="email-btn"></div>
  <div class="share">Share with us</div>
  <div class="social-foot"><span style="background:#2f5fa8"></span><span style="background:#2fa9e0"></span><span style="background:#f07a1e"></span></div>
  <div class="vline" style="left:851px"></div>
  <h4 style="left:883px;top:38px">Contact Us</h4>
  <ul class="foot-list" style="left:883px;top:62px">
    <li>Mobile: 1234567890</li><li>Phone: 1234567890</li><li>eMail: brenwickit.com</li>
  </ul>
  <div class="rule" style="left:0;top:222px;width:1200px;background:#3d3d3d"></div>
  <div class="copyright">Copyright &copy; 2013 BrenwickIT.com .all right reserved. | Privacy Policy</div>
</footer>

</body>
</html>
```